Crestline Delivery Partners Business Card Redesign Project

CRESTLINE DELIVERY PARTNERS
Our company needs to have its business cards redesigned as the current design no longer reflects the business brand or attracts the type of clientele we are seeking.

MUST LOOK
★ Upmarket
★ Reflect Quality
★ Corporate feel
★ Professional
★ Innovative
★ Colourful

MUST PROMOTE
★ Market Leader
★ Knowledge
★ Expertise
★ Experience
★ Solutions
★ Advice

MUST FEEL
★ Classy
★ Elegant
★ Savvy
★ Edgy
★ Upbeat

WHAT WE DO
Crestline Delivery Partners provides project management and project controls consultancy services to companies in many industry sectors, within Australia and overseas. My company has developed a business brand through forging strong business relationships within industry. We provide innovative tools, concepts and solutions to management teams to assist them in better plan and managing there project portfolios.

SECTORS OF INDUSTRY WE SERVICE
★Oil & Gas
★Minerals & Metals
★Petrochemical
★Manufacturing
★Building & Construction
★Telecommunications
★Rail
★Civil

BUSINESS CARD DETAILS REQUIRED ON FRONT
Marcus Feldwick
Business Owner
Tel: 0498357162
Email: marcusfeldwick@crestlinedeliverypartners.com
Website: www.crestlinedeliverypartners.com.au

BUSINESS CARD DETAILS REQUIRED ON BACK
Providing | Knowledge | Expertise | Experience

ATTACHMENTS
Business Logo

Target Market(s)

Oil & Gas I Mining & Resources I Industry in General
Upmarket Clientele
Corporate World

Industry/Entity Type

Industry

Requirements
Must have
• Must be creative and a unique design
The business card must have information on the front and back

```html
<!DOCTYPE html>
<html lang="en">
<head>
<meta charset="utf-8">
<title>Crestline Delivery Partners – Business Card</title>
<link rel="stylesheet" href="https://fonts.googleapis.com/css2?family=Jost:wght@400;500;600;700&display=swap">
<style>
  :root {
    --stage: #3b3b3d;
    --card-white: #fbfbfb;
    --card-dark: #151516;
    --card-dark-edge: #232325;
    --ink: #1d1d1f;
    --ink-soft: #4a4a4d;
    --accent-red: #e3232f;
    --back-text: #bdbdc0;
    --brand-light: #f4f4f4;
  }
  * { box-sizing: border-box; margin: 0; padding: 0; }
  html, body { width: 1200px; height: 900px; overflow: hidden; }
  body {
    background: var(--stage);
    font-family: "Jost", "Futura", sans-serif;
    display: flex;
    flex-direction: column;
    align-items: center;
    justify-content: center;
    gap: 44px;
  }
  .card {
    position: relative;
    width: 680px;
    height: 388px;
    border-radius: 4px;
    box-shadow: 0 14px 34px rgba(0,0,0,0.45);
    overflow: hidden;
  }

  /* Back of card */
  .card--back { background: var(--card-dark); }
  .card--back .texture {
    position: absolute; inset: 0;
    background: radial-gradient(ellipse at 50% 40%, var(--card-dark-edge) 0%, var(--card-dark) 70%);
  }
  .card--back .brand {
    position: absolute;
    top: 150px; left: 0; right: 0;
    display: flex; align-items: center; justify-content: center; gap: 14px;
    color: var(--brand-light);
    font-weight: 600;
    font-size: 26px;
    letter-spacing: 2px;
  }
  .brand-square {
    width: 18px; height: 18px;
    background: var(--accent-red);
  }
  .card--back .values {
    position: absolute;
    bottom: 52px; left: 0; right: 0;
    text-align: center;
    color: var(--back-text);
    font-weight: 400;
    font-size: 17px;
    letter-spacing: 1.4px;
  }

  /* Front of card */
  .card--front { background: var(--card-white); }
  .card--front .brand-block {
    position: absolute;
    top: 50px; right: 44px;
    text-align: left;
  }
  .card--front .brand {
    display: flex; align-items: center; gap: 10px;
    color: var(--ink);
    font-weight: 700;
    font-size: 25px;
    letter-spacing: 0.5px;
    line-height: 1;
  }
  .card--front .brand .brand-square { width: 22px; height: 22px; }
  .card--front .strapline {
    margin-top: 6px;
    margin-left: 32px;
    color: var(--ink-soft);
    font-size: 10.5px;
    font-weight: 500;
    letter-spacing: 0.3px;
  }
  .contact {
    position: absolute;
    top: 200px; right: 44px;
    display: flex;
    font-size: 15px;
    line-height: 21px;
  }
  .contact-labels {
    text-align: right;
    color: var(--accent-red);
    font-weight: 600;
    padding-right: 8px;
    border-right: 1.5px solid var(--ink);
  }
  .contact-values {
    padding-left: 8px;
    color: var(--ink-soft);
    font-weight: 400;
  }
  .contact-values .phone { font-size: 17px; letter-spacing: 0.5px; }
  .person {
    position: absolute;
    left: 46px; bottom: 50px;
  }
  .person-name {
    color: var(--ink);
    font-weight: 600;
    font-size: 28px;
    line-height: 1.1;
  }
  .person-role {
    color: var(--accent-red);
    font-weight: 400;
    font-size: 20px;
    line-height: 1.2;
  }
</style>
</head>
<body>

  <section class="card card--back" aria-label="Business card, back">
    <div class="texture" role="img" aria-label="Dark glossy card surface with subtle tone pattern"></div>
    <div class="brand"><span class="brand-square"></span>CRESTLINE DELIVERY PARTNERS</div>
    <p class="values">Providing | Knowledge | Expertise | Experience</p>
  </section>

  <section class="card card--front" aria-label="Business card, front">
    <div class="brand-block">
      <div class="brand"><span class="brand-square"></span>CRESTLINE DELIVERY PARTNERS</div>
      <p class="strapline">Providing Effective Project Controls and Management Solutions</p>
    </div>

    <div class="contact">
      <div class="contact-labels">
        <div>Phone</div>
        <div>Email</div>
        <div>Website</div>
      </div>
      <div class="contact-values">
        <div class="phone">0498357162</div>
        <div>marcusfeldwick@crestlinedeliverypartners.com</div>
        <div>www.crestlinedeliverypartners.com</div>
      </div>
    </div>

    <div class="person">
      <h1 class="person-name">Marcus Feldwick</h1>
      <p class="person-role">Business Owner</p>
    </div>
  </section>

</body>
</html>
```